Soft furnishing company selling fabrics, curtains, bedlinen craft & haberdashery

We need 4 x home page banners for our website as follows:
Image 1 - to lead customers to our "New season Fabrics" page,
Image 2 - to lead customers to our Ready Made curtains,
Image 3 - to lead customers to our "Polar Bear Bed linen" page
Image 4 - to lead customers to our "Christmas raft Tutorial" page

Banner needs to be 960px wide x 380px 72dpi and optimised for web. should have a little descriptive text for example "Fabulous Fabric. Prints, plains & weaves, view our range of new season furnishing fabrics to buy by the metre" "Instantly update your home with our range of ready made curtains. Available . "Cosy Night In. Snuggle with this Polar Bear Duvet Set. From €20" "" "Let's Get Crafting for Christmas. Download our free Project and tutoirals here. First 3 images need a "shop now" button

website url www.lintelnest.ie

Target Market(s)

Female 25 -45

Industry/Entity Type

It Company

Font styles to use
Serif
Sans Serif

Requirements
Must have
• shop now button on image 1, 2, 3
Should not have
• too much text or clutter

```html
<!DOCTYPE html>
<html lang="en">
<head>
<meta charset="utf-8">
<title>Lintel Nest – Home Page Banners</title>
<link rel="stylesheet" href="https://fonts.googleapis.com/css2?family=Arimo:wght@400&family=Montserrat:wght@800&family=Dancing+Script:wght@500&display=swap">
<style>
  :root {
    --page: #ffffff;
    --white: #ffffff;
    --slate: #4e5064;
    --slate-dark: #2c2e3b;
    --slate-band: #3a3c4d;
    --tan: #b08c72;
    --tan-band: #8f705a;
    --taupe: #a39483;
    --taupe-band: #857767;
    --red: #ec1c24;
    --red-band: #c8141b;
    --fabric-photo: linear-gradient(135deg, #c9a48c 0%, #b8898a 35%, #9aa1a7 60%, #5d4a3e 100%);
    --curtain-photo: linear-gradient(90deg, #7a5a3a 0%, #5a4a46 30%, #4f4447 60%, #cfc9bd 85%, #8b7f70 100%);
    --bear-photo: linear-gradient(120deg, #d8d2c9 0%, #ece9e5 40%, #c9c3bb 70%, #8c8279 100%);
    --craft-photo: radial-gradient(ellipse at 35% 55%, #efe6dc 0%, #f5eeea 35%, #ffffff 70%);
    --button: #141414;
  }
  * { box-sizing: border-box; margin: 0; padding: 0; }
  html, body { width: 1200px; height: 1000px; overflow: hidden; background: var(--page); }
  .canvas { position: relative; width: 1200px; height: 1000px; font-family: "Arimo", Arial, sans-serif; }

  .banner { position: absolute; }
  .banner-photo { position: absolute; left: 0; top: 0; }
  .caption {
    position: absolute; left: 0; height: 25px;
    color: var(--white); font-size: 7.5px; letter-spacing: .1px;
    display: flex; align-items: center;
  }
  .side-panel { position: absolute; top: 0; }
  .pattern-band { position: absolute; left: 0; right: 0; height: 25px; }
  .pattern-band.top { top: 0; }
  .pattern-band.bottom { bottom: 0; }

  .title-frame {
    position: absolute; border: 1.5px solid var(--white);
    color: var(--white); font-size: 16.5px; line-height: 18px;
    display: flex; align-items: center; justify-content: center; text-align: center;
  }
  .cta {
    position: absolute; height: 18px; border-radius: 5px;
    background: linear-gradient(180deg, #4a4a4a 0%, var(--button) 50%, #000 100%);
    box-shadow: 0 0 0 1px #9a8a6a, 1px 2px 2px rgba(0,0,0,.45);
    color: var(--white); font-family: "Montserrat", Arial, sans-serif; font-weight: 800;
    font-size: 9px; letter-spacing: .2px;
    display: flex; align-items: center; justify-content: center;
  }

  /* Banner 1 – New Season Fabrics */
  .fabrics { left: 318px; top: 32px; width: 566px; height: 223px; }
  .fabrics .banner-photo { width: 392px; height: 200px; background: var(--fabric-photo); }
  .fabrics .caption { top: 198px; width: 392px; background: var(--slate-dark); padding-left: 10px; }
  .fabrics .side-panel { left: 392px; width: 174px; height: 223px; background: var(--slate); }
  .fabrics .pattern-band { background: var(--slate-band); }
  .fabrics .title-frame { left: 46px; top: 67px; width: 86px; height: 70px; }
  .fabrics .cta { left: 57px; top: 162px; width: 61px; }

  /* Banner 2 – Ready Made Curtains */
  .curtains { left: 318px; top: 268px; width: 567px; height: 223px; }
  .curtains .banner-photo { width: 393px; height: 198px; background: var(--curtain-photo); }
  .curtains .caption { top: 198px; width: 393px; background: var(--tan); justify-content: center; }
  .curtains .side-panel { left: 393px; width: 174px; height: 223px; background: var(--tan); }
  .curtains .pattern-band { background: var(--tan-band); }
  .curtains .title-frame { left: 46px; top: 68px; width: 86px; height: 70px; }
  .curtains .cta { left: 57px; top: 162px; width: 61px; }

  /* Banner 3 – Polar Bear Bed Linen */
  .bedlinen { left: 319px; top: 505px; width: 567px; height: 223px; }
  .bedlinen .banner-photo { width: 393px; height: 198px; background: var(--bear-photo); }
  .bedlinen .caption { top: 198px; width: 393px; background: var(--taupe); justify-content: center; }
  .bedlinen .side-panel { left: 393px; width: 174px; height: 223px; background: var(--taupe); }
  .bedlinen .pattern-band { background: var(--taupe-band); }
  .bedlinen .title-frame { left: 35px; top: 68px; width: 102px; height: 70px; }
  .bedlinen .cta { left: 56px; top: 162px; width: 62px; }

  /* Banner 4 – Christmas Craft Tutorial */
  .craft { left: 318px; top: 742px; width: 568px; height: 235px; }
  .craft .banner-photo { left: 20px; top: 8px; width: 345px; height: 222px; background: var(--craft-photo); }
  .craft-intro {
    position: absolute; left: 126px; top: 32px;
    font-family: "Dancing Script", cursive; font-size: 13px; line-height: 17px;
    color: var(--red); transform: rotate(-1.5deg);
  }
  .craft .side-panel { left: 385px; width: 183px; height: 235px; background: var(--red); }
  .craft .pattern-band { background: var(--red-band); }
  .craft .pattern-band.bottom { height: 27px; }
  .craft .title-frame { left: 37px; top: 71px; width: 106px; height: 73px; }
  .craft .cta { left: 59px; top: 161px; width: 65px; }
</style>
</head>
<body>
<main class="canvas">

  <section class="banner fabrics">
    <div class="banner-photo" role="img" aria-label="Stack of folded patterned furnishing fabrics with autumn leaves blowing around"></div>
    <p class="caption">Fabulous fabric. prints, plains &amp; weaves, view our range of new season furnishing fabrics to buy by the metre.</p>
    <div class="side-panel">
      <div class="pattern-band top" role="img" aria-label="Geometric triangle pattern band"></div>
      <h2 class="title-frame">New<br>Season<br>Fabrics</h2>
      <a class="cta">SHOP NOW</a>
      <div class="pattern-band bottom" role="img" aria-label="Geometric triangle pattern band"></div>
    </div>
  </section>

  <section class="banner curtains">
    <div class="banner-photo" role="img" aria-label="Living room with tartan ready made curtains, leather armchair and wall clock"></div>
    <p class="caption">Instantly update your home with our range of ready made curtains.</p>
    <div class="side-panel">
      <div class="pattern-band top" role="img" aria-label="Geometric triangle pattern band"></div>
      <h2 class="title-frame">Ready<br>Made<br>Curtains</h2>
      <a class="cta">SHOP NOW</a>
      <div class="pattern-band bottom" role="img" aria-label="Geometric triangle pattern band"></div>
    </div>
  </section>

  <section class="banner bedlinen">
    <div class="banner-photo" role="img" aria-label="Bedroom with polar bear print duvet set, pillows and cushions"></div>
    <p class="caption">Cosy Night In. Snuggle with this Polar Bear Duvet Set. From €20.</p>
    <div class="side-panel">
      <div class="pattern-band top" role="img" aria-label="Geometric triangle pattern band"></div>
      <h2 class="title-frame">Polar Bear<br>Bed<br>linen</h2>
      <a class="cta">SHOP NOW</a>
      <div class="pattern-band bottom" role="img" aria-label="Geometric triangle pattern band"></div>
    </div>
  </section>

  <section class="banner craft">
    <div class="banner-photo" role="img" aria-label="Handmade fabric reindeer pulling a red fabric sleigh"></div>
    <p class="craft-intro">Let's Get Crafting for Christmas.<br>Download our free Project and tutoirals here.</p>
    <div class="side-panel">
      <div class="pattern-band top" role="img" aria-label="Geometric triangle pattern band"></div>
      <h2 class="title-frame">Christmas<br>Craft<br>Tutorial</h2>
      <a class="cta">DOWNLOAD</a>
      <div class="pattern-band bottom" role="img" aria-label="Geometric triangle pattern band"></div>
    </div>
  </section>

</main>
</body>
</html>
```